Attract customers for New Zealand forest eco tour

Website design for a new eco tourism business in New Zealand. We have domain name booked for it: www.GlenofTavi.co.nz

We have written the site, see attachments. And have all the pictures to go with it, have just attached a few of these for examples. Will provide the rest to the winning bidder.

We want the look of the site to be highly visually attractive, clean and uncluttered. And if you know about what works best for eco-tourism, that will help.

Website should be mobile phone readable, as well as desktop.

Our objectives for the site are to introduce our forest to them, get people interested in visiting, and have people book trips. We will need some kind of booking app such as with dates of bookings, and ideally a payment app as well so they can pay for bookings.

Ideally, I don't know if you can do this, you use a format which allows us to self edit the site (note, we're not technical experts).

Target Market(s)

Professional people aged 30 - 49.
Looking to travel, probably as a couple.
International travel for adventure, relaxation.

Key things they want are:

See attractions
Go to a place different from their own country
Escape from their usual working life
Unwind and relax

Industry/Entity Type

Business

Coding

Coded - Design and coding required

Number of Pages Required

5+ page

Colors
9bcb3b

Requirements
Must have
• Visually attractive - pictorial look
• Clean and uncluttered - blank space
• Mobile readable and desktop
• Booking app
• Payment app
Nice to have
• Be self editable by us (non-technical people)
Should not have
• shouldn't look cheap

```html
<!DOCTYPE html>
<html lang="en">
<head>
<meta charset="utf-8">
<title>Glen of Tavi</title>
<link rel="stylesheet" href="https://fonts.googleapis.com/css2?family=Source+Sans+3:wght@400;600;700&display=swap">
<style>
:root{
  --green:#9bcb3b;
  --green-dark:#7fae25;
  --orange:#e8650f;
  --ink:#333;
  --muted:#666;
  --grey-title:#6b6f73;
  --footer:#2a2a2a;
  --line:#d9d9d9;
}
*{box-sizing:border-box;margin:0;padding:0}
html,body{width:1200px;height:2768px;overflow:hidden}
body{font-family:"Source Sans 3",Arial,sans-serif;color:var(--ink);background:#fff;position:relative}
.section{position:absolute;left:0;width:1200px}

/* hero */
.hero{top:0;height:560px;background:linear-gradient(180deg,#3c4a4a 0%,#56676a 30%,#6b7f7a 55%,#3f5446 80%,#24301f 100%)}
.nav-bar{position:absolute;top:0;left:0;width:100%;height:64px;background:rgba(0,0,0,.25)}
.brand{position:absolute;left:108px;top:12px;font-size:34px;font-weight:700;color:var(--green)}
.nav{position:absolute;right:100px;top:20px;display:flex;gap:26px;list-style:none}
.nav li{color:#fff;font-size:16px}
.nav li.active{color:var(--green);border-bottom:2px solid var(--green);padding-bottom:4px}
.hero-text{position:absolute;top:240px;width:100%;text-align:center;color:#fff}
.hero-text h1{font-size:38px;font-weight:600}
.hero-text p{font-size:21px;margin-top:2px}
.btn-ghost{display:inline-block;margin-top:22px;border:1px solid var(--green);color:#fff;font-size:14px;padding:6px 20px}

/* tours */
.tours{top:608px;height:160px}
.tour-card{position:absolute;top:0;width:476px;height:152px;background:linear-gradient(135deg,#d7dde6,#eef1f5 50%,#cfd6e0);text-align:center;padding-top:14px;border:1px solid #e2e2e2}
.tour-card h2{font-size:38px;font-weight:400;color:var(--grey-title)}
.tour-card p{font-size:14px;color:var(--muted)}
.btn{display:inline-block;background:var(--orange);color:#fff;font-size:15px;padding:5px 20px;margin-top:10px}

/* project */
.project{top:812px;height:236px;background:var(--green);text-align:center;color:#fff}
.project h2{font-size:34px;font-weight:700;margin-top:32px}
.project p{width:900px;margin:18px auto 0;font-size:13px;line-height:1.5}
.project .btn{margin-top:18px}

/* activities */
.activities{top:1100px;height:520px;text-align:center}
.section-title{font-size:36px;font-weight:700}
.activities .section-title{color:var(--orange)}
.section-sub{font-size:15px;color:var(--muted);width:560px;margin:4px auto 0;line-height:1.3}
.activity-grid{position:absolute;top:100px;left:100px;width:1000px;display:grid;grid-template-columns:repeat(4,1fr);row-gap:34px}
.activity{display:flex;flex-direction:column;align-items:center}
.activity-icon{width:124px;height:124px;border-radius:50%;background:var(--orange)}
.activity h3{font-size:16px;font-weight:700;margin-top:12px;width:170px;line-height:1.15}

/* attractions */
.attractions{top:1620px;height:440px;background:linear-gradient(180deg,#4a5a6e 0%,#6a7a8a 35%,#5c6a55 70%,#3f4a3a 100%);text-align:center;color:#fff}
.attractions .section-title{margin-top:36px;color:#fff}
.attractions .section-sub{color:#eee;width:800px}
.attraction-card{position:absolute;top:140px;width:312px;height:220px;background:linear-gradient(160deg,#6b8fa8,#8b6a4a 55%,#3b5a4a)}
.tag{position:absolute;top:12px;left:12px;background:var(--green);color:#fff;font-size:12px;padding:3px 10px}
.card-caption{position:absolute;left:0;bottom:28px;width:100%;background:rgba(155,203,59,.85);text-align:left;padding:6px 14px;font-size:17px}
.date-badge{position:absolute;right:14px;bottom:14px;width:70px;height:70px;border-radius:50%;background:var(--orange);border:3px solid #fff;display:flex;flex-direction:column;align-items:center;justify-content:center;font-weight:700;line-height:1}
.date-badge b{font-size:20px}
.date-badge small{font-size:11px}

/* contact */
.contact{top:2060px;height:380px}
.contact .section-title{text-align:center;color:#444;font-weight:600;margin-top:38px}
.info{position:absolute;left:112px;width:300px}
.info dt{position:absolute;left:0;color:var(--green-dark);font-weight:700;font-size:15px}
.info dd{position:absolute;left:150px;font-size:13px;color:var(--muted);line-height:1.5;width:170px}
.field{position:absolute;border:1px solid var(--line);background:#fff}
.field svg{position:absolute;left:8px;top:10px}
.send{position:absolute;left:888px;top:300px;width:180px;height:40px;border:1px solid var(--green);color:var(--green-dark);font-size:14px;text-align:center;line-height:38px;background:#fff}

/* map */
.map{top:2440px;height:280px;background:linear-gradient(135deg,#e6eadf,#d9e4cf 40%,#c8d8e8 75%,#e9ece4)}

/* footer */
.footer{top:2720px;height:48px;background:var(--footer);color:#ddd;font-size:14px}
.footer p{position:absolute;left:112px;top:14px}
.social{position:absolute;right:112px;top:9px;display:flex;gap:8px}
.social span{width:30px;height:30px;background:#555}
</style>
</head>
<body>

<header class="section hero" role="img" aria-label="Coastal forest headland at dusk">
  <div class="nav-bar">
    <div class="brand">Glen of Tavi</div>
    <ul class="nav">
      <li class="active">Home</li><li>About Us</li><li>Tours</li><li>Project</li><li>Activities</li><li>Gallery</li><li>Contact US</li>
    </ul>
  </div>
  <div class="hero-text">
    <h1>welcome to our site</h1>
    <p>Glen of Tavi is a beautiful native forest in the Far North of New Zealand</p>
    <span class="btn-ghost">Contact Now</span>
  </div>
</header>

<section class="section tours">
  <article class="tour-card" style="left:112px">
    <h2>OVERNIGHT TOURS</h2>
    <p>Around 1 kilometre into the forest we have a camp set up.</p>
    <span class="btn">Read more</span>
  </article>
  <article class="tour-card" style="left:612px">
    <h2>DAY TRIPS TOURS</h2>
    <p>If you'd like to spend a day in the forest you'll love this.</p>
    <span class="btn">Read more</span>
  </article>
</section>

<section class="section project">
  <h2>OUR PROJECT</h2>
  <p>In the far north, our forest shelters native birds, ancient trees and rare plants. We are restoring the land with local help, planting trees, clearing pests and sharing the quiet beauty of this place with visitors who care for nature as we do.</p>
  <span class="btn">Read more</span>
</section>

<section class="section activities">
  <h2 class="section-title">OUR ACTIVITIES</h2>
  <p class="section-sub">You can do what you like as activities. These are some of things we enjoy, and visitors to the forest we've had really</p>
  <div class="activity-grid">
    <div class="activity"><div class="activity-icon" role="img" aria-label="Tree icon"></div><h3>GRANDFATHER OF THE FOREST</h3></div>
    <div class="activity"><div class="activity-icon" role="img" aria-label="Owl icon"></div><h3>BIRDWATCHER</h3></div>
    <div class="activity"><div class="activity-icon" role="img" aria-label="Coconut drink icon"></div><h3>FOREST GOURMET</h3></div>
    <div class="activity"><div class="activity-icon" role="img" aria-label="Crayfish icon"></div><h3>CRAYFISH HUNTER</h3></div>
    <div class="activity"><div class="activity-icon" role="img" aria-label="Forest walker icon"></div><h3>FORESTMAN</h3></div>
    <div class="activity"><div class="activity-icon" role="img" aria-label="Orchid icon"></div><h3>ORCHID OBSESSIVE</h3></div>
    <div class="activity"><div class="activity-icon" role="img" aria-label="Spider icon"></div><h3>PURIRI GIANT LEGS</h3></div>
    <div class="activity"><div class="activity-icon" role="img" aria-label="Tree climber icon"></div><h3>TREE GURU</h3></div>
  </div>
</section>

<section class="section attractions" role="img" aria-label="Blurred coastal landscape">
  <h2 class="section-title">LOCAL ATTRACTIONS</h2>
  <p class="section-sub">If you're coming to this part of the country, there are some awesome local attractions nearby</p>
  <div class="attraction-card" style="left:112px" role="img" aria-label="Beach cove with rock arch">
    <span class="tag">21 JULY</span><div class="card-caption">Lorem ipsum dolor</div>
    <div class="date-badge"><b>25</b><small>DATE</small></div>
  </div>
  <div class="attraction-card" style="left:444px" role="img" aria-label="Beach cove with rock arch">
    <span class="tag">21 JULY</span><div class="card-caption">Lorem ipsum dolor</div>
    <div class="date-badge"><b>25</b><small>DATE</small></div>
  </div>
  <div class="attraction-card" style="left:776px" role="img" aria-label="Beach cove with rock arch">
    <span class="tag">21 JULY</span><div class="card-caption">Lorem ipsum dolor</div>
    <div class="date-badge"><b>25</b><small>DATE</small></div>
  </div>
</section>

<section class="section contact">
  <h2 class="section-title">CONTACT US</h2>
  <dl class="info" style="top:120px">
    <dt style="top:0">Our Address</dt>
    <dd style="top:0">Lorem ipsum dolor sit amet, consectetur adipiscing elit.</dd>
    <dt style="top:96px">Phone Number</dt>
    <dd style="top:96px">1800-00-0000<br>1800-00-0000</dd>
    <dt style="top:160px">Email Id</dt>
    <dd style="top:160px">hello@glenoftavi.co.nz<br>bookings@glenoftavi.co.nz</dd>
  </dl>
  <div class="field" style="left:452px;top:110px;width:300px;height:40px">
    <svg width="18" height="18" viewBox="0 0 18 18"><circle cx="9" cy="6" r="4" fill="#aaa"/><path d="M2 17c0-4 3-6 7-6s7 2 7 6z" fill="#aaa"/></svg>
  </div>
  <div class="field" style="left:768px;top:110px;width:320px;height:40px">
    <svg width="20" height="16" viewBox="0 0 20 16"><rect x="1" y="2" width="18" height="12" fill="none" stroke="#aaa" stroke-width="2"/><path d="M1 2l9 7 9-7" fill="none" stroke="#aaa" stroke-width="2"/></svg>
  </div>
  <div class="field" style="left:452px;top:170px;width:636px;height:176px">
    <svg width="18" height="18" viewBox="0 0 18 18"><path d="M2 2h14v10H7l-4 4v-4H2z" fill="none" stroke="#aaa" stroke-width="2"/></svg>
  </div>
  <div class="send">Send a Message</div>
</section>

<section class="section map" role="img" aria-label="Street map of the forest area"></section>

<footer class="section footer">
  <p>Copyright © 2015 lorem ipsum dolor</p>
  <div class="social"><span></span><span></span><span></span><span></span></div>
</footer>

</body>
</html>
```